Creative/innovative law firm website

A law firm website that immediately looks different from other law firm websites. We like the color scheme (dark background with warm, neutral colors) and simple, organic logos (trees, leaves, etc.) of this website: https://brambleworth.legal/

We'll be offering creative/innovative solutions to complex problems faced by state governments, industries, other law firms, and individuals. We're located in Montana (U.S.A.), and the outdoors is a huge part of our lives and identities.

We will need a home page, an "About Us" page with a separate subpage for each attorney (two attorneys), a blog or "Publications" page, a payment portal (which will integrate with Quillo), and a "Services" page.

```html
<!DOCTYPE html>
<html lang="en">
<head>
<meta charset="utf-8">
<title>Harrow &amp; Whitcombe P.C — Montana Law Firm</title>
<link rel="stylesheet" href="https://fonts.googleapis.com/css2?family=Tinos:ital,wght@0,400;0,700;1,400&family=Montserrat:ital,wght@0,400;0,500;0,600;0,700;1,400&display=swap">
<style>
:root{
  --red:#c9351f;
  --ink:#0d0d0d;
  --bg-1:#121212;
  --card:#1f1f1f;
  --line:#2c2c2c;
  --white:#ffffff;
  --muted:#c9c9c9;
  --dim:#8f8f8f;
}
*{box-sizing:border-box;margin:0;padding:0}
html,body{width:1200px;height:4955px;overflow:hidden;background:var(--ink)}
body{font-family:"Montserrat",sans-serif;color:var(--white);position:relative}
.serif{font-family:"Tinos",serif}
.abs{position:absolute}
section,header,footer{position:absolute;left:0;width:1200px}
.btn{position:absolute;background:var(--red);color:#fff;font-size:13px;font-weight:600;letter-spacing:.3px;display:flex;align-items:center;justify-content:center;gap:6px;text-transform:uppercase;white-space:nowrap}
.btn::after{content:"";border-left:5px solid #fff;border-top:4px solid transparent;border-bottom:4px solid transparent}
.btn.ghost{background:transparent}
.label{position:absolute;color:var(--red);font-size:12px;letter-spacing:.5px;text-transform:uppercase;display:flex;align-items:center;gap:14px}
.label::before{content:"";width:38px;height:1px;background:var(--red)}
.label.center{left:0;width:1200px;justify-content:center}
.h2{position:absolute;font-family:"Tinos",serif;font-size:36px;line-height:1.1;font-weight:400;white-space:nowrap}
.h2.center{left:0;width:1200px;text-align:center}
.photo{position:absolute}

/* header */
.topbar{top:0;height:110px;background:var(--ink)}
.brand{position:absolute;left:38px;top:18px;display:flex;align-items:center;gap:18px}
.brand-mark{width:70px;height:70px;border:3px solid var(--red);border-radius:50%}
.brand-name{font-family:"Tinos",serif;font-size:23px;letter-spacing:.5px}
.brand-sub{font-size:12px;color:var(--muted);margin-top:4px}
.cta-top{left:935px;top:0;width:219px;height:38px;font-size:15px}
.cta-top::after{display:none}
.phone-top{left:935px;top:56px;font-size:30px;font-weight:500;letter-spacing:.5px;white-space:nowrap}
.nav{top:110px;left:115px;width:972px;height:48px;background:#050505;border-radius:0 0 12px 12px;z-index:3}
.nav a{position:absolute;top:16px;color:#fff;text-decoration:none;font-size:14px;font-weight:500}
.search{position:absolute;left:703px;top:9px;width:230px;height:30px;border-left:1px solid #2a2a2a;display:flex;align-items:center;padding-left:14px;font-size:12px;color:var(--dim)}
.search svg{position:absolute;right:10px;top:9px}

/* hero */
.hero{top:110px;height:717px}
.hero .photo{left:0;top:0;width:1200px;height:717px;background:linear-gradient(90deg,#1c1c1c 0%,#3a3a3a 45%,#6b6b6b 70%,#2b2b2b 100%)}
.hero-fade{position:absolute;left:0;bottom:0;width:1200px;height:160px;background:linear-gradient(180deg,rgba(18,18,18,0),var(--bg-1))}
.hero-title{position:absolute;left:150px;top:232px;font-size:54px;line-height:1;letter-spacing:1px;font-weight:400}
.hero-text{position:absolute;left:150px;top:362px;width:470px;font-size:15px;line-height:24px;font-weight:500}
.hero .btn{left:150px;top:438px;width:154px;height:38px}

/* about */
.about{top:827px;height:596px;background:var(--bg-1)}
.about .photo{left:144px;top:58px;width:398px;height:453px;background:linear-gradient(160deg,#9a9a9a,#4a4a4a 60%,#2a2a2a)}
.award{position:absolute;left:144px;top:442px;width:187px;height:69px;background:var(--red);display:flex;align-items:center;gap:10px;padding-left:14px;font-size:13px;line-height:17px}
.about .label{left:602px;top:80px}
.about .h2{left:600px;top:112px;font-size:35px}
.about-text{position:absolute;left:600px;top:222px;width:460px;font-size:13px;line-height:22.5px;color:var(--muted)}
.stat{position:absolute;font-size:13px;display:flex;align-items:center;gap:8px;white-space:nowrap}
.about .btn{left:600px;top:450px;width:156px;height:36px}

/* practice */
.practice{top:1423px;height:615px}
.practice .photo{left:0;top:0;width:1200px;height:615px;background:linear-gradient(180deg,#151515,#1c1c1c 50%,#101010)}
.service{position:absolute;top:198px;height:264px;background:#191919;text-align:center}
.service svg{margin-top:28px}
.service h3{font-size:19px;font-weight:600;margin-top:22px}
.service p{font-size:13.5px;line-height:20px;color:var(--muted);margin:14px auto 0;width:250px}
.service .more{position:absolute;left:0;right:0;bottom:24px;color:var(--red);font-size:13px;display:flex;justify-content:center;align-items:center;gap:6px;text-transform:uppercase}
.more::after{content:"";border-left:5px solid var(--red);border-top:4px solid transparent;border-bottom:4px solid transparent}
.practice .btn{left:508px;top:496px;width:184px;height:35px}

/* why */
.why{top:2038px;height:554px;background:var(--ink)}
.why-block{position:absolute;left:869px;top:6px;width:331px;height:548px;background:var(--red)}
.why .photo{left:698px;top:96px;width:340px;height:366px;background:linear-gradient(170deg,#b8b8b8,#6b6b6b 55%,#3b3b3b)}
.why .label{left:150px;top:85px}
.why .h2{left:150px;top:114px;font-size:36px}
.why-text{position:absolute;left:150px;top:212px;width:500px;font-size:13.5px;line-height:23px;color:var(--muted)}
.quote{position:absolute;left:194px;top:278px;width:460px;font-size:14.5px;font-style:italic;line-height:25px}
.quote-mark{position:absolute;left:148px;top:270px;font-family:"Tinos",serif;font-size:60px;line-height:1;font-style:italic}
.why .btn{left:150px;top:408px;width:140px;height:35px}

/* team */
.team{top:2592px;height:442px;background:linear-gradient(180deg,#1a1a1a,#121212)}
.member{position:absolute;top:164px;width:427px;height:190px;background:#1d1d1d}
.member .photo{left:6px;top:6px;width:150px;height:178px}
.member h3{position:absolute;left:173px;top:26px;font-family:"Tinos",serif;font-size:19px;font-weight:400;letter-spacing:.5px}
.member .role{position:absolute;left:173px;top:55px;font-size:11px;color:var(--red)}
.member p{position:absolute;left:173px;top:80px;width:235px;font-size:13px;line-height:21px;color:var(--muted)}
.member .more{position:absolute;left:173px;top:152px;color:var(--red);font-size:13px;display:flex;align-items:center;gap:6px;text-transform:uppercase}

/* blog */
.blog{top:3034px;height:643px;background:#1b1b1b}
.post{position:absolute;top:164px;width:275px}
.post .photo{position:relative;width:275px;height:183px}
.post h3{font-size:15.5px;font-weight:600;margin-top:32px;white-space:nowrap}
.meta{display:flex;gap:18px;font-size:10.5px;margin-top:14px;align-items:center}
.meta span{display:flex;align-items:center;gap:6px}
.post p{font-size:12px;line-height:20px;color:var(--muted);margin-top:12px;text-align:justify}
.post .btn{position:absolute;top:371px;left:0;width:128px;height:35px;font-size:12px}
.post .btn.ghost{background:#1b1b1b}

/* clients */
.clients{top:3677px;height:377px;background:#131313}
.client{position:absolute;top:165px;width:158px;height:96px;background:#1c1c1c;display:flex;align-items:center;justify-content:center;gap:8px;font-size:20px;font-weight:600;color:#fff;white-space:nowrap}
.dots{position:absolute;left:0;width:1200px;top:294px;display:flex;justify-content:center;gap:6px}
.dots i{width:11px;height:11px;border:1.5px solid #bbb;border-radius:50%}
.dots i.on{background:var(--red);border-color:var(--red)}

/* map */
.map{top:4054px;height:436px}
.map .photo{left:0;top:0;width:1200px;height:436px;background:linear-gradient(135deg,#2d2d2d,#262626 50%,#303030)}
.addr{position:absolute;left:15px;top:17px;width:327px;height:69px;background:#121212;font-size:12.5px;line-height:18px;padding:16px 0 0 18px}
.addr svg{position:absolute;right:18px;top:24px}
.pin{position:absolute;left:586px;top:262px}

/* contact band */
.contact{top:4490px;height:112px;background:var(--red)}
.contact-mid{position:absolute;left:417px;top:0;width:366px;height:112px;background:#121212}
.c-item{position:absolute;top:36px;display:flex;align-items:center;gap:16px;white-space:nowrap}
.c-item small{display:block;font-size:11px;margin-bottom:4px}
.c-item b{font-size:18px;font-weight:600}

/* footer */
.footer{top:4602px;height:353px;background:var(--ink)}
.f-brand{position:absolute;left:140px;top:70px;width:274px;text-align:center}
.f-mark{width:100px;height:100px;border:3px solid var(--red);border-radius:50%;margin:0 auto}
.f-brand .n{font-family:"Tinos",serif;font-size:18px;margin-top:18px;white-space:nowrap}
.f-brand .s{font-size:11.5px;color:var(--muted);margin-top:2px}
.f-col{position:absolute;top:74px}
.f-col h4{font-family:"Tinos",serif;font-weight:400;font-size:18px;letter-spacing:.5px;margin-bottom:14px}
.f-col li{list-style:none;font-size:13px;line-height:27px;color:var(--muted)}
.f-col p{font-size:12.5px;line-height:20px;color:var(--muted);width:230px}
.f-input{position:absolute;left:829px;top:164px;width:221px;height:27px;background:#050505;border:1px solid #2a2a2a;font-size:11.5px;padding:6px 10px}
.f-submit{position:absolute;left:829px;top:205px;width:84px;height:27px;background:var(--red);font-size:11.5px;font-weight:600;display:flex;align-items:center;justify-content:center}
.f-rule{position:absolute;left:150px;top:282px;width:900px;height:1px;background:var(--line)}
.copy{position:absolute;left:150px;top:309px;font-size:12.5px;color:var(--muted)}
.cards{position:absolute;left:827px;top:300px;display:flex;gap:4px}
.cards span{width:52px;height:30px;background:#e8e8e8;color:#1a1a1a;font-size:10px;font-weight:600;display:flex;align-items:center;justify-content:center}
</style>
</head>
<body>

<header class="topbar">
  <div class="brand">
    <div class="brand-mark"></div>
    <div>
      <div class="brand-name">HARROW &amp; WHITCOMBE P.C</div>
      <div class="brand-sub">LAW FIRM, LLC</div>
    </div>
  </div>
  <div class="btn cta-top">FREE CONSULTATION</div>
  <div class="abs phone-top">(406) 555 0142</div>
</header>

<nav class="abs nav">
  <a style="left:33px">HOME</a>
  <a style="left:110px">ABOUT US</a>
  <a style="left:218px">PRACTICE AREAS</a>
  <a style="left:377px">PUBLICATIONS</a>
  <a style="left:519px">CONTACT US</a>
  <div class="search">Search
    <svg width="12" height="12" viewBox="0 0 12 12"><circle cx="5" cy="5" r="3.8" fill="none" stroke="#fff" stroke-width="1.6"/><path d="M8 8l3 3" stroke="#fff" stroke-width="1.8"/></svg>
  </div>
</nav>

<section class="hero">
  <div class="photo" role="img" aria-label="Black and white photo of a lawyer in a suit reading a book in a library"></div>
  <div class="hero-fade"></div>
  <h1 class="hero-title serif">HARROW &amp;<br>WHITCOMBE P.C</h1>
  <p class="hero-text">Creative answers to complex legal problems, built in Montana where the outdoors shapes how we think.</p>
  <div class="btn">Read More</div>
</section>

<section class="about">
  <div class="photo" role="img" aria-label="Black and white photo of two colleagues working at a laptop"></div>
  <div class="award">
    <svg width="30" height="30" viewBox="0 0 30 30"><circle cx="15" cy="13" r="9" fill="none" stroke="#fff" stroke-width="1.6"/><path d="M10 20l-3 8 5-2 3 3 0-7M20 20l3 8-5-2-3 3" fill="none" stroke="#fff" stroke-width="1.4"/></svg>
    <span>Award Winning<br>Lawyer</span>
  </div>
  <div class="label">About Us</div>
  <h2 class="h2">INNOVATIVE COUNSEL FOR<br>COMPLEX PROBLEMS</h2>
  <p class="about-text">From our base in Montana we help state governments, industries, fellow law firms and individuals solve problems that do not fit a template. We bring fresh thinking, plain talk and the patience of people who spend their weekends in the mountains, and we stay with each matter until the path forward is clear.</p>
  <div class="stat" style="left:600px;top:364px">✎ 20+ Yr Experience</div>
  <div class="stat" style="left:795px;top:364px">✎ Awards Winning</div>
  <div class="stat" style="left:600px;top:400px">✎ 500+ Happy Clients</div>
  <div class="stat" style="left:795px;top:400px">✎ 1000+ Completed Works</div>
  <div class="btn">Read More</div>
</section>

<section class="practice">
  <div class="photo" role="img" aria-label="Dark faded photo of a law library"></div>
  <div class="label center" style="top:90px">Services</div>
  <h2 class="h2 center" style="top:122px">OUR PRACTICE AREA</h2>
  <div class="service" style="left:150px;width:296px">
    <svg width="60" height="52" viewBox="0 0 60 52" fill="none" stroke="#c9351f" stroke-width="2.4"><path d="M6 46h48M10 46V22M22 46V22M38 46V22M50 46V22M4 20L30 6l26 14z"/></svg>
    <h3>GOVERNMENT LAW</h3>
    <p>Practical, creative counsel for state agencies facing new and complex policy questions.</p>
    <div class="more">Learn More</div>
  </div>
  <div class="service" style="left:460px;width:282px">
    <svg width="60" height="52" viewBox="0 0 60 52" fill="none" stroke="#c9351f" stroke-width="2.4"><path d="M4 48h52M8 48V28l12-8v8l12-8v8l12-8v28M46 48V10h6v38"/></svg>
    <h3>INDUSTRY COUNSEL</h3>
    <p>Fresh solutions for energy, land, agriculture and outdoor businesses across the West.</p>
    <div class="more">Learn More</div>
  </div>
  <div class="service" style="left:769px;width:285px">
    <svg width="60" height="52" viewBox="0 0 60 52" fill="none" stroke="#c9351f" stroke-width="2.4"><rect x="8" y="14" width="44" height="30"/><path d="M22 14V6h16v8M8 26h44M30 22v10"/></svg>
    <h3>FIRM &amp; PERSONAL</h3>
    <p>Partnering with other law firms and individuals on problems that need new thinking.</p>
    <div class="more">Learn More</div>
  </div>
  <div class="btn">View All Services</div>
</section>

<section class="why">
  <div class="why-block"></div>
  <div class="photo" role="img" aria-label="Black and white photo of a smiling attorney in an office"></div>
  <div class="label">Why Choose Us?</div>
  <h2 class="h2">Innovative, Practical Solutions<br>from Big Sky Country.</h2>
  <p class="why-text">We look at every problem from a new angle, the same way a trail looks different at every turn of the season.</p>
  <div class="quote-mark">“</div>
  <p class="quote">Complex problems rarely have a standard answer. Our work is to find the one that fits, explain it plainly and carry it through, for the state, the industry or the neighbour down the road.</p>
  <div class="btn">Read More</div>
</section>

<section class="team">
  <div class="label center" style="top:75px">Attorneys</div>
  <h2 class="h2 center" style="top:106px">Meet Our Team</h2>
  <div class="member" style="left:150px">
    <div class="photo" role="img" aria-label="Portrait photo of attorney Harrow in a library" style="background:linear-gradient(160deg,#6b4a2e,#3a2a1c)"></div>
    <h3>HARROW</h3>
    <div class="role">FOUNDER, PUBLIC LAW</div>
    <p>Guides state agencies and industries through new legal ground with calm, creative strategy.</p>
    <div class="more">View Profile</div>
  </div>
  <div class="member" style="left:625px">
    <div class="photo" role="img" aria-label="Portrait photo of attorney Whitcombe" style="background:linear-gradient(160deg,#cfcac4,#6a5e58)"></div>
    <h3>WHITCOMBE</h3>
    <div class="role">PARTNER, LITIGATION</div>
    <p>Builds fresh solutions for firms and individuals facing complex, high-stakes disputes.</p>
    <div class="more">View Profile</div>
  </div>
</section>

<section class="blog">
  <div class="label center" style="top:68px">News</div>
  <h2 class="h2 center" style="top:100px">Our Blog Posts</h2>
  <article class="post" style="left:150px">
    <div class="photo" role="img" aria-label="Black and white photo of a gavel beside pills" style="background:linear-gradient(170deg,#9a9a9a,#2c2c2c)"></div>
    <h3>Water rights in a dry year</h3>
    <div class="meta"><span><svg width="10" height="10"><rect width="10" height="10" fill="#c9351f"/></svg>Nov 13, 2021</span><span><svg width="10" height="10"><circle cx="5" cy="5" r="5" fill="#c9351f"/></svg>OWEN CARVER</span></div>
    <p>How ranchers, towns and the state can share a shrinking supply without ending up in years of court.</p>
    <div class="btn ghost">Read More</div>
  </article>
  <article class="post" style="left:461px">
    <div class="photo" role="img" aria-label="Black and white photo of scales of justice and a gavel" style="background:linear-gradient(170deg,#e0e0e0,#6e6e6e)"></div>
    <h3>New paths for public land</h3>
    <div class="meta"><span><svg width="10" height="10"><rect width="10" height="10" fill="#c9351f"/></svg>Oct 31, 2021</span><span><svg width="10" height="10"><circle cx="5" cy="5" r="5" fill="#c9351f"/></svg>OWEN CARVER</span></div>
    <p>Access, recreation and resource use can live side by side when agreements are drafted with care.</p>
    <div class="btn">Read More</div>
  </article>
  <article class="post" style="left:775px">
    <div class="photo" role="img" aria-label="Black and white photo of a handshake behind scales of justice" style="background:linear-gradient(170deg,#d4d4d4,#3a3a3a)"></div>
    <h3>When firms team up on a case</h3>
    <div class="meta"><span><svg width="10" height="10"><rect width="10" height="10" fill="#c9351f"/></svg>Oct 13, 2021</span><span><svg width="10" height="10"><circle cx="5" cy="5" r="5" fill="#c9351f"/></svg>OWEN CARVER</span></div>
    <p>Co-counsel work brings new ideas to old problems. Here is how we keep shared matters clear and fair.</p>
    <div class="btn ghost">Read More</div>
  </article>
</section>

<section class="clients">
  <div class="label center" style="top:77px">News</div>
  <h2 class="h2 center" style="top:109px">Our Clients</h2>
  <div class="client" style="left:150px">Meridex</div>
  <div class="client" style="left:335px">Caselark</div>
  <div class="client" style="left:520px"><svg width="18" height="18"><circle cx="9" cy="9" r="9" fill="#fff"/></svg>Verdo</div>
  <div class="client" style="left:705px">Tallis Suite</div>
  <div class="client" style="left:890px"><svg width="16" height="16"><rect width="16" height="16" fill="#fff"/></svg>Pellora</div>
  <div class="dots"><i></i><i></i><i class="on"></i><i></i><i></i></div>
</section>

<section class="map">
  <div class="photo" role="img" aria-label="Dark street map of Bozeman showing the office location"></div>
  <div class="addr">210 Ridge Avenue, Bozeman,<br>Montana – MT 59715
    <svg width="24" height="18" viewBox="0 0 24 18"><path d="M14 2l8 7-8 7v-4Q6 12 2 17q1-9 12-10z" fill="#fff"/></svg>
  </div>
  <svg class="pin" width="28" height="38" viewBox="0 0 28 38"><path d="M14 1C6 1 1 7 1 14c0 10 13 23 13 23s13-13 13-23C27 7 22 1 14 1z" fill="#fff"/><circle cx="14" cy="14" r="5" fill="#2a2a2a"/></svg>
</section>

<section class="contact">
  <div class="contact-mid"></div>
  <div class="c-item" style="left:150px">
    <svg width="38" height="38" viewBox="0 0 38 38"><path d="M9 4l6 8-4 4q4 8 11 11l4-4 8 6-4 6Q16 34 4 10z" fill="#fff"/></svg>
    <div><small>Send Us A Message</small><b>(+1) 406 555 0142</b></div>
  </div>
  <div class="c-item" style="left:450px">
    <svg width="42" height="32" viewBox="0 0 42 32"><rect x="1" y="4" width="40" height="26" fill="none" stroke="#fff" stroke-width="2.4"/><path d="M1 4l20 15L41 4" fill="none" stroke="#fff" stroke-width="2.4"/></svg>
    <div><small>Send Us A Message</small><b>info@harrowwhitcombe.com</b></div>
  </div>
  <div class="c-item" style="left:800px">
    <svg width="28" height="38" viewBox="0 0 28 38"><path d="M14 1C6 1 1 7 1 14c0 10 13 23 13 23s13-13 13-23C27 7 22 1 14 1z" fill="#fff"/><circle cx="14" cy="14" r="5" fill="#c9351f"/></svg>
    <div><small>Office Location</small><b>Bozeman, Montana, USA.</b></div>
  </div>
</section>

<footer class="footer">
  <div class="f-brand">
    <div class="f-mark"></div>
    <div class="n">HARROW &amp; WHITCOMBE P.C</div>
    <div class="s">LAW FIRM, LLC</div>
  </div>
  <div class="f-col" style="left:461px">
    <h4>QUICK LINKS</h4>
    <ul><li>Home</li><li>About us</li><li>Services</li><li>Publications</li><li>Contact</li></ul>
  </div>
  <div class="f-col" style="left:640px">
    <h4>USEFUL LINKS</h4>
    <ul><li>Privacy Policy</li><li>Terms &amp; Conditions</li><li>Disclaimer</li><li>Support</li><li>FAQ</li></ul>
  </div>
  <div class="f-col" style="left:829px">
    <h4>NEWSLETTER</h4>
    <p>Fresh ideas and legal news from Montana, once a month.</p>
  </div>
  <div class="f-input">Enter Email</div>
  <div class="f-submit">SUBMIT</div>
  <div class="f-rule"></div>
  <div class="copy">Copyrights © 2021 Harrow &amp; Whitcombe P.C. All Rights Reserved.</div>
  <div class="cards"><span>Paycrest</span><span>Novi</span><span>Amerline</span><span>Findra</span></div>
</footer>

</body>
</html>
```